Brighten up our Patty Hut Retail Menus

We are a large family-run, food company located in Papua New Guinea and sell a wide range of products. We have 3x Comet Patty Huts and all items are in-house manufactured by our Butchery and Bakery. We are fun, bold and colourful! The Comet Patty colours are Blue and Yellow and our overarching company colours are Red and Black.

Our current menu board is attached in size 120cm (h) x 200cm(w).
Our menu is for display in our retail in 2 sizes (portrait and landscape) and online. We currently feel this is too dark, messy and difficult to read. We want to target our customer base - where photos are a key point for sales! Font and size need to be readable from afar. Text content/grouping should be the same as our previous one. We also want to keep it modern. We are open to a variety of original designs/layouts.

Logos, photos and menu items are attached.
Follow our website - www.klq.com.pg for more information.

Please don't hesitate to ask any questions! Thank you and we can't wait for you to join our project.

Target Market(s)

Economical

Industry/Entity Type

Fast Food

Colors
0054AA
0677BA
7BADD7
CADEEF
E8F1F8
FFF300
FFF600
FEFA6F
FFFEC7
FFFEE8

Requirements
Must have
• Images as the key point of sale, clear to read.
Nice to have
• Inviting, bright, bold, playful
Should not have
• Dark, difficult to read

```html
<!DOCTYPE html>
<html lang="en">
<head>
<meta charset="utf-8">
<title>Comet Patty Menu</title>
<link href="https://fonts.googleapis.com/css2?family=Archivo+Black&family=Poppins:wght@400;500;600;700&display=swap" rel="stylesheet">
<style>
:root{
  --orange:#eba21d;
  --blue:#1e47a4;
  --ink:#1d1d1d;
  --muted:#555;
  --paper:#ffffff;
  --backdrop:#e3e3e3;
}
*{box-sizing:border-box;margin:0;padding:0}
html,body{width:867px;height:1200px;overflow:hidden}
body{background:var(--backdrop);font-family:"Poppins",sans-serif;color:var(--ink);position:relative}
.menu{position:absolute;left:0;top:340px;width:867px;height:520px;background:var(--paper);box-shadow:0 6px 18px rgba(0,0,0,.18)}
.col{position:absolute}
.band{position:absolute;background:var(--orange);color:#fff;font-family:"Archivo Black",sans-serif;font-size:19px;line-height:1;padding:4px 7px 0;letter-spacing:.2px;white-space:nowrap;overflow:hidden}
.sub{font-family:"Poppins",sans-serif;font-weight:700;color:var(--blue);font-size:8px;margin:4px 0 3px}
.row{display:flex;align-items:baseline;font-size:7px;font-weight:600;line-height:1.25;white-space:nowrap}
.row .dots{flex:1;border-bottom:1px dotted #666;margin:0 2px;min-width:4px}
.price{color:var(--blue);font-weight:600}
.desc{font-size:4.3px;color:var(--muted);line-height:1.25;margin-bottom:5px;font-weight:400}
.stack .row{margin-bottom:6.5px}
.photo{position:absolute;border-radius:10px}
.brand{position:absolute;left:42px;top:62px;width:160px;text-align:center;font-family:"Archivo Black",sans-serif;color:var(--blue);font-size:27px;line-height:1.05}
.brand-dot{position:absolute;left:106px;top:28px;width:28px;height:28px;border-radius:50%;background:var(--orange)}
.framed{position:absolute;border:1.5px solid #9a9a9a;border-radius:8px;padding:8px 12px}
.framed h3{font-family:"Archivo Black",sans-serif;color:var(--blue);font-size:16px;text-align:center;line-height:1;margin-bottom:6px}
.note{font-size:6.5px;font-weight:600;line-height:1.2}
.note b{color:var(--blue);font-weight:600}
.thumbs{display:flex;gap:6px;justify-content:center;margin-top:6px}
.thumbs span{width:45px;height:34px;border:1.5px solid var(--orange);background:linear-gradient(#f1c27a,#b9672e)}
</style>
</head>
<body>
<main class="menu">

  <div class="brand-dot"></div>
  <div class="brand">Comet Patty</div>

  <!-- Left: breakfast -->
  <div class="band" style="left:31px;top:181px;width:174px;height:26px">BURGER</div>
  <section class="col" style="left:31px;top:214px;width:174px">
    <div class="sub">BREKKIE TOASTIE</div>
    <div class="row">Chicken &amp; Cheese<span class="dots"></span><span>K13.00</span></div>
    <div class="desc">Roast Chicken with aioli &amp; melted cheese, toasted<br>using our bakers bread of the day</div>
    <div class="row">Ham &amp; Cheese<span class="dots"></span><span>K13.00</span></div>
    <div class="desc">Ham &amp; melted cheese, toasted using our bakers<br>bread of the day</div>
    <div class="row">Maple Ham &amp; Cheese Croissant<span class="dots"></span><span>K12.00</span></div>
    <div class="desc">Maple Ham with melted swiss cheese in a freshly<br>baked &amp; toasted croissant</div>
    <div class="sub">COSMO BREAKFAST MUFFIN</div>
    <div class="row">Sausages &amp; Egg Muffin<span class="dots"></span><span>K12.00</span></div>
    <div class="desc">Toasted english muffin with char grilled sausage<br>patty, fried egg, cheddar slice and bbq sauce</div>
    <div class="row">Bacon &amp; Egg Muffin<span class="dots"></span><span>K12.00</span></div>
    <div class="desc">Bacon, egg and cheese with bbq sauce on a toasted<br>english muffin</div>
    <div class="row">Hash Browns<span class="dots"></span><span>K5.00</span></div>
    <div class="desc">2 x crunchy potato deliciousness</div>
    <div class="row">Brekky Meal Deal<span class="dots"></span><span>Just Add</span></div>
    <div class="row" style="font-size:4.3px;font-weight:400;color:var(--muted);margin-bottom:3px">Make your breakfast into a meal (with coffee and<span class="dots" style="border:0"></span><span style="font-size:7px;font-weight:600;color:var(--ink)">K8.00 Tasol</span></div>
    <div class="note">(this means that's all) Save K2.50<br><b>Available until 10am Everyday</b></div>
  </section>
  <div class="photo" role="img" aria-label="Breakfast toasties and muffins" style="left:45px;top:448px;width:160px;height:46px;background:linear-gradient(90deg,#c46a3a,#e9c27a 60%,#f0b640)"></div>

  <!-- Burgers, wraps & more -->
  <div class="band" style="left:221px;top:31px;width:419px;height:27px">BURGERS, WRAPS &amp; MORE</div>
  <section class="col stack" style="left:221px;top:67px;width:96px">
    <div class="row">Cheese Burger<span class="dots"></span><span class="price">K20.00</span></div>
    <div class="row">Aussie Burger<span class="dots"></span><span class="price">K25.00</span></div>
    <div class="row">Kiwi Deluxe<span class="dots"></span><span class="price">K24.00</span></div>
    <div class="row">Comet Burger<span class="dots"></span><span class="price">K30.00</span></div>
    <div class="row">Crunchy Chicken<span class="dots"></span><span class="price">K20.00</span></div>
    <div class="row" style="margin-bottom:0">Upgrade to a meal</div>
    <div class="row" style="margin-bottom:1px">deal - large<span class="dots"></span><span class="price">K17.00</span></div>
    <div class="desc">Chips + either a 330ml can drink,<br>juice or 400ml water</div>
    <div class="row" style="margin-bottom:0">Upgrade to a meal</div>
    <div class="row">deal - small<span class="dots"></span><span class="price">K12.00</span></div>
  </section>
  <section class="col stack" style="left:326px;top:67px;width:98px">
    <div class="row">The Hangover<span class="dots"></span><span class="price">K28.00</span></div>
    <div class="row">Steak Sandwich<span class="dots"></span><span class="price">K26.00</span></div>
    <div class="row">BLT + C Sandwich<span class="dots"></span><span class="price">K14.00</span></div>
  </section>
  <div class="photo" role="img" aria-label="Stacked beef burger with bacon and cheese" style="left:328px;top:115px;width:98px;height:96px;border-radius:50%;background:radial-gradient(circle at 50% 40%,#e3a14c,#7a3a1d 70%,#ffffff 72%)"></div>
  <section class="col stack" style="left:439px;top:67px;width:201px">
    <div class="row">Comet Chips - large<span class="dots"></span><span class="price">K15.00</span></div>
    <div class="row">Comet Chips - small<span class="dots"></span><span class="price">K10.00</span></div>
    <div class="row">Loaded Wedges Chicken<span class="dots"></span><span class="price">K15.00</span></div>
    <div class="row">Loaded Wedges Pork<span class="dots"></span><span class="price">K15.00</span></div>
    <div class="row">Wraps - Veggie<span class="dots"></span><span class="price">K10.00</span></div>
    <div class="row">Wraps - Chicken<span class="dots"></span><span class="price">K22.00</span></div>
    <div class="row">Wraps - Lamb<span class="dots"></span><span class="price">K30.00</span></div>
  </section>
  <div class="photo" role="img" aria-label="Chicken wrap" style="left:446px;top:180px;width:50px;height:36px;background:linear-gradient(#ecd3a4,#c98a4c)"></div>
  <div class="photo" role="img" aria-label="Cup of chips" style="left:510px;top:178px;width:28px;height:40px;background:linear-gradient(#f1b13b,#d0843a)"></div>
  <div class="photo" role="img" aria-label="Loaded wedges" style="left:552px;top:186px;width:84px;height:30px;background:linear-gradient(90deg,#e7c05a,#b64a2a,#e7c05a)"></div>

  <!-- Boxes -->
  <div class="band" style="left:221px;top:215px;width:201px;height:26px">COMET BOXES</div>
  <section class="col" style="left:221px;top:250px;width:203px">
    <div class="row">Comet Nibbles &amp; Chips<span class="dots"></span><span class="price">K40.00</span></div>
    <div class="desc">1/2 kilo crumbed chicken nibbles with garlic aioli<br>and comet dipping sauce</div>
    <div class="row">3 Pc Chicken<span class="dots"></span><span class="price">K36.00</span></div>
    <div class="desc">3 tender pieces of bone-in chicken in southern style<br>crumb served with comet chips, bread roll &amp; gravy</div>
    <div class="row">Chicken Nuggets<span class="dots"></span><span class="price">K15.00</span></div>
    <div class="desc">8 x chicken nuggets with tomato sauce</div>
    <div class="row">Chicken Bucket<span class="dots"></span><span class="price">K125.00</span></div>
    <div class="desc" style="display:flex;justify-content:space-between;margin-bottom:3px">18 pcs of southern fried chicken<span class="price" style="font-size:7px">Tasol</span></div>
    <div class="row">Upgrade your chicken bucket to a family</div>
    <div class="row">meal deal<span class="dots"></span><span class="price">K45.00</span></div>
    <div class="desc" style="display:flex;justify-content:space-between">2 x large chips, 1 x 1 ltr soft drink, 1 x coleslaw<span class="price" style="font-size:7px">Tasol</span></div>
  </section>
  <section class="framed" style="left:226px;top:381px;width:192px;height:90px">
    <h3>KIDS MEAL</h3>
    <div class="row">Chicken / Beef / Fish<span class="dots"></span><span class="price">K22.00</span></div>
    <div class="desc" style="margin-bottom:0">Kids burger comes with juice box, small chips and a toy</div>
    <div class="thumbs" role="img" aria-label="Kids chicken, beef and fish burgers"><span></span><span></span><span></span></div>
  </section>

  <!-- Dessert -->
  <div class="band" style="left:439px;top:225px;width:201px;height:26px">DESSERT</div>
  <section class="col" style="left:439px;top:264px;width:122px">
    <div class="row" style="margin-bottom:6px">Sundae<span class="dots"></span><span class="price">K9.00 Tasol</span></div>
    <div class="row" style="margin-bottom:6px">Ice Cream Cone<span class="dots"></span><span class="price">K7.00 Tasol</span></div>
    <div class="row">Add On's - Syrups<span class="dots"></span><span class="price">K1.50 per</span></div>
    <div class="desc" style="display:flex;justify-content:space-between">Vanilla / Chocolate /<br>Strawberry<span class="price" style="font-size:7px;font-weight:600">syrup</span></div>
    <div class="row">Milkshakes<span class="dots"></span><span class="price">K14.00 Tasol</span></div>
    <div class="desc">Vanilla, chocolate, banana,<br>strawberry &amp; caramel</div>
    <div class="row">Thickshakes<span class="dots"></span><span class="price">K16.00 Tasol</span></div>
    <div class="desc">Strawberry, chocolate,<br>vanilla, caramel &amp; banana</div>
  </section>
  <div class="photo" role="img" aria-label="Soft serve ice cream cone and sundae cup" style="left:566px;top:258px;width:74px;height:107px;background:linear-gradient(#f4f4f2,#dfe3e8 60%,#e1b877)"></div>

  <!-- Hot beverages -->
  <div class="band" style="left:439px;top:375px;width:208px;height:26px">HOT BEVERAGES</div>
  <section class="col" style="left:439px;top:411px;width:88px">
    <div class="row" style="margin-bottom:5px">Cappuccino<span class="dots"></span><span class="price">K8.00</span></div>
    <div class="row" style="margin-bottom:5px">Flat White<span class="dots"></span><span class="price">K8.00</span></div>
    <div class="row" style="margin-bottom:5px">Latte<span class="dots"></span><span class="price">K8.00</span></div>
    <div class="row" style="margin-bottom:5px">Hot Chocolate<span class="dots"></span><span class="price">K8.00</span></div>
    <div class="row">Mocha<span class="dots"></span><span class="price">K8.00</span></div>
  </section>
  <section class="col" style="left:540px;top:411px;width:98px">
    <div class="row" style="margin-bottom:5px">Long Black<span class="dots"></span><span class="price">K6.50</span></div>
    <div class="row" style="margin-bottom:5px">Babyccino<span class="dots"></span><span class="price">K5.00</span></div>
    <div class="row" style="margin-bottom:5px">Black Tea<span class="dots"></span><span class="price">K6.50</span></div>
    <div class="row" style="margin-bottom:5px">Extra Shot Coffee<span class="dots"></span><span class="price">K2.90</span></div>
    <div class="row">Extra Sugar<span class="dots"></span><span class="price">K0.20</span></div>
  </section>

  <!-- Drinks -->
  <div class="band" style="left:656px;top:31px;width:179px;height:27px">DRINKS</div>
  <section class="col stack" style="left:656px;top:67px;width:100px">
    <div class="row">All 500ml Drinks<span class="dots"></span><span class="price">K5.00</span></div>
    <div class="row">All 300ml Drinks<span class="dots"></span><span class="price">K4.00</span></div>
    <div class="row">Pure Water 700ml<span class="dots"></span><span class="price">K2.50</span></div>
    <div class="row">Pure Water 400ml<span class="dots"></span><span class="price">K3.50</span></div>
    <div class="row">Earth Spring 600ml<span class="dots"></span><span class="price">K3.00</span></div>
  </section>
  <section class="col stack" style="left:765px;top:67px;width:70px">
    <div class="row">Viva Juice<span class="dots"></span><span class="price">K2.80</span></div>
    <div class="row">Pure Zest<span class="dots"></span><span class="price">K2.80</span></div>
    <div class="row">Volt Energy<span class="dots"></span><span class="price">K6.00</span></div>
  </section>

  <section class="framed" style="left:659px;top:148px;width:176px;height:107px;padding:8px 14px">
    <h3>DIPPING SAUCE</h3>
    <div class="row" style="margin-bottom:4px">Tomato<span class="dots"></span><span class="price">K3.00</span></div>
    <div class="row" style="margin-bottom:4px">BBQ<span class="dots"></span><span class="price">K3.00</span></div>
    <div class="row" style="margin-bottom:4px">Comet Hot<span class="dots"></span><span class="price">K3.00</span></div>
    <div class="row" style="margin-bottom:4px">Garlic Aioli<span class="dots"></span><span class="price">K3.00</span></div>
    <div class="row">Sweet Chili<span class="dots"></span><span class="price">K3.00</span></div>
  </section>

  <!-- Add ons -->
  <div class="band" style="left:656px;top:261px;width:179px;height:27px">ADD ON'S</div>
  <section class="col stack" style="left:656px;top:298px;width:80px">
    <div class="row">Cheese slice<span class="dots"></span><span class="price">K2.00</span></div>
    <div class="row">Onion rings<span class="dots"></span><span class="price">K3.00</span></div>
    <div class="row">Beetroot slice<span class="dots"></span><span class="price">K2.00</span></div>
    <div class="row">Bacon<span class="dots"></span><span class="price">K3.00</span></div>
  </section>
  <section class="col stack" style="left:742px;top:298px;width:93px">
    <div class="row">Egg<span class="dots"></span><span class="price">K3.00</span></div>
    <div class="row">Extra beef patty<span class="dots"></span><span class="price">K10.00</span></div>
    <div class="row">Extra lamb patty<span class="dots"></span><span class="price">K13.50</span></div>
    <div class="row">Extra Sauce<span class="dots"></span><span class="price">K2.00</span></div>
  </section>
  <div class="photo" role="img" aria-label="Crispy chicken burger beside a double beef burger" style="left:666px;top:375px;width:190px;height:137px;border-radius:40% 40% 20% 20%;background:radial-gradient(ellipse at 50% 45%,#e3a14c,#8a4420 65%,#ffffff 70%)"></div>
</main>
</body>
</html>
```